Eye Catching Tamber Vale van wrap with branding to be important

Create a professional, clean, and premium-looking ¾ wrap that makes the van instantly recognizable as Tamber Vale , a high-end outdoor lighting company specializing in landscape, permanent holiday, and temporary holiday lighting. We would like to see the color palette of the logo used. The design should communicate elegance, trust, and expertise — not clutter or gimmicks. Our logo is the brand and would like that to be remembered above all.

we have a slogan that you may use if wanted " See your home in a whole new light....at night"

our phone number is 555-013-2846 and our website is www.TAMBER-VALE.com

Target Market(s)

High end clients

Industry/Entity Type

Outdoor Lighting

Colors
FFF300
FFF600
FEFA6F
FFFEC7
FFFEE8
FFC000
F8CF3A
FAE287
FDF2CF
FEFAEE

Requirements
Must have
• 3/4 wrap- not a full wrap
Nice to have
• Somehow get the point out that we do lighting without having to spell it out would be nice?
Should not have
• any other colors other than brand colors

```html
<!DOCTYPE html>
<html lang="en">
<head>
<meta charset="utf-8">
<title>Tamber Vale – Van Wrap Side Panel</title>
<link rel="stylesheet" href="https://fonts.googleapis.com/css2?family=Montserrat:wght@700;800&family=Poppins:ital,wght@1,600&display=swap">
<style>
  :root {
    --canvas: #ffffff;
    --wrap-black: #000000;
    --roof-grey: #55555c;
    --amber: #ffc000;
    --gold: #f8cf3a;
    --lemon: #fff300;
    --pale: #fef
    --text-white: #ffffff;
    --text-grey: #6d6d73;
  }
  html, body {
    margin: 0;
    width: 1200px;
    height: 900px;
    overflow: hidden;
    background: var(--canvas);
  }
  .wrap-panel {
    position: absolute;
    left: 50px;
    top: 209px;
    width: 1100px;
    height: 481px;
  }
  .panel-black { fill: var(--wrap-black); }
  .roof-band { fill: var(--roof-grey); }
  .stripe-amber { fill: var(--amber); }
  .stripe-gold { fill: var(--gold); }
  .stripe-lemon { fill: var(--lemon); }
  .phone {
    font-family: "Montserrat", sans-serif;
    font-weight: 800;
    font-size: 40px;
    letter-spacing: -2px;
    fill: var(--text-white);
    stroke: var(--text-grey);
    stroke-width: 1.4px;
    paint-order: stroke;
  }
  .website {
    font-family: "Montserrat", sans-serif;
    font-weight: 800;
    font-size: 37px;
    letter-spacing: -2px;
    fill: var(--text-grey);
    stroke: var(--text-white);
    stroke-width: 1.4px;
    paint-order: stroke;
  }
  .slogan {
    font-family: "Poppins", sans-serif;
    font-style: italic;
    font-weight: 600;
    font-size: 21px;
    fill: var(--text-white);
  }
  .slogan .accent { fill: var(--amber); }
  .home-scene { fill: var(--wrap-black); }
</style>
</head>
<body>
<svg class="wrap-panel" viewBox="0 0 800 350" xmlns="http://www.w3.org/2000/svg">
  <!-- roof band and light stripes -->
  <polygon class="roof-band" points="260,18 525,8 366,108"/>
  <polygon class="stripe-amber" points="90,18 170,18 315,141 271,170"/>
  <polygon class="stripe-gold" points="170,18 230,18 349,119 315,141"/>
  <polygon class="stripe-lemon" points="230,18 260,18 366,108 349,119"/>

  <!-- main black panel -->
  <path class="panel-black" d="M0,347 L525,6 L760,0 Q790,0 795,30 L800,350 L0,350 Z"/>

  <!-- light cone over home -->
  <g class="light-cone">
    <polygon class="stripe-amber" points="485,105 260,242 710,242"/>
    <polygon class="stripe-gold" points="485,105 330,242 640,242"/>
    <polygon class="stripe-lemon" points="485,105 400,242 570,242"/>
  </g>
  <rect class="home-scene" x="398" y="172" width="162" height="70" role="img" aria-label="Silhouette of a house with a lit window between two trees"/>

  <!-- contact -->
  <text class="phone" x="203" y="64">555-013-2846</text>
  <text class="website" x="180" y="291">www.TAMBER-VALE.com</text>

  <!-- slogan -->
  <text class="slogan" text-anchor="end">
    <tspan x="741" y="42">See your</tspan>
    <tspan x="741" y="77">home in a</tspan>
    <tspan x="748" y="112">whole new light</tspan>
    <tspan class="accent" x="748" y="147">… at night!</tspan>
  </text>
</svg>
</body>
</html>
```